Business Card Design

New company looking for logo, for business cards and email signature.
we provide Safety, Training and Project Management Services to Mining and Transport sectors.

Industry/Entity Type

Business

Contact Information for Business Card

HOLLOWAY CONSULTANCY, Tom Westcott, Principal Consultant, 0491362284, hollowayconsultancy@examplemail.test , Unit 214,Kestrel Point Trade Centre,581 Tamsin Street, Corrindale, 4862.
Steady Operations built on Safe Practice, Skills and Guidance.

```html
<!DOCTYPE html>
<html lang="en">
<head>
<meta charset="utf-8">
<title>Holloway Consultancy – Business Card</title>
<link rel="stylesheet" href="https://fonts.googleapis.com/css2?family=Open+Sans:wght@400;600&display=swap">
<style>
  :root {
    --teal: #2b6580;
    --teal-deep: #245a73;
    --mark: #86a6b8;
    --ink: #2a3a44;
    --muted: #9aa3a8;
    --paper: #ffffff;
    --backdrop: #e9ebec;
  }
  * { box-sizing: border-box; margin: 0; padding: 0; }
  html, body { width: 1200px; height: 900px; overflow: hidden; }
  body {
    background: var(--backdrop);
    font-family: "Open Sans", Arial, sans-serif;
    display: flex;
    flex-direction: column;
    align-items: center;
    justify-content: center;
    gap: 44px;
  }
  .card {
    position: relative;
    width: 660px;
    height: 377px;
    border-radius: 4px;
    box-shadow: 0 10px 28px rgba(0,0,0,.14);
    overflow: hidden;
  }
  .brand {
    display: flex;
    align-items: center;
    gap: 16px;
  }
  .brand-square { width: 58px; height: 58px; flex: none; }
  .brand-name {
    font-weight: 400;
    font-size: 27px;
    letter-spacing: 1.5px;
    white-space: nowrap;
  }

  /* back of card */
  .card-back {
    background: var(--teal);
    display: flex;
    align-items: center;
    justify-content: center;
  }
  .card-back .brand-square { background: var(--mark); }
  .card-back .brand-name { color: var(--paper); }

  /* front of card */
  .card-front { background: var(--paper); }
  .card-front .brand {
    position: absolute;
    left: 150px;
    top: 50px;
  }
  .card-front .brand-square { background: var(--mark); }
  .card-front .brand-name { color: var(--teal); }

  .contact {
    position: absolute;
    left: 318px;
    top: 158px;
    color: var(--ink);
    font-size: 14.5px;
    line-height: 22px;
  }
  .contact-line { display: flex; align-items: center; gap: 7px; white-space: nowrap; }
  .contact-line svg { width: 14px; height: 14px; flex: none; }

  .person {
    position: absolute;
    left: 72px;
    top: 232px;
  }
  .person-name {
    color: var(--teal);
    font-weight: 600;
    font-size: 19px;
    line-height: 24px;
  }
  .person-role {
    color: var(--muted);
    font-size: 14px;
    line-height: 20px;
  }

  .tagline-band {
    position: absolute;
    left: 0; right: 0; bottom: 0;
    height: 52px;
    background: var(--teal-deep);
    color: var(--paper);
    font-size: 16px;
    display: flex;
    align-items: center;
    justify-content: center;
    letter-spacing: .2px;
  }
</style>
</head>
<body>

  <section class="card card-back">
    <div class="brand">
      <div class="brand-square"></div>
      <div class="brand-name">HOLLOWAY CONSULTANCY</div>
    </div>
  </section>

  <section class="card card-front">
    <div class="brand">
      <div class="brand-square"></div>
      <div class="brand-name">HOLLOWAY CONSULTANCY</div>
    </div>

    <div class="contact">
      <div class="contact-line">Unit 214,Kestrel Point Trade Centre</div>
      <div class="contact-line">581 Tamsin Street, Corrindale, 4862.</div>
      <div class="contact-line">
        <svg viewBox="0 0 24 24" aria-hidden="true"><path fill="#2a3a44" d="M6.6 10.8a15.2 15.2 0 0 0 6.6 6.6l2.2-2.2a1 1 0 0 1 1-.25 11.4 11.4 0 0 0 3.6.57 1 1 0 0 1 1 1V20a1 1 0 0 1-1 1A17 17 0 0 1 3 4a1 1 0 0 1 1-1h3.5a1 1 0 0 1 1 1c0 1.25.2 2.45.57 3.6a1 1 0 0 1-.25 1z"/></svg>
        <span>0491362284</span>
      </div>
      <div class="contact-line">
        <svg viewBox="0 0 24 24" aria-hidden="true"><rect x="2" y="5" width="20" height="14" fill="#2a3a44"/><path d="M2.5 5.5 12 13l9.5-7.5" fill="none" stroke="#fff" stroke-width="1.6"/></svg>
        <span>hollowayconsultancy@examplemail.test</span>
      </div>
    </div>

    <div class="person">
      <div class="person-name">Tom Westcott</div>
      <div class="person-role">Principal Consultant</div>
    </div>

    <div class="tagline-band">Steady Operations built on Safe Practice, Skills and Guidance.</div>
  </section>

</body>
</html>
```